Mesh Banner Design for Business Premises

We require the design of a large mesh banner to be installed across the front fence of our warehouse. The banner should prominently feature our existing Rigmore logo and brand colours (yellow, white, and black) and be designed to be highly visible from the road.

The overall aesthetic should be strong, masculine, and industrial, reflecting the nature of the scaffolding and construction industry. The background should be predominantly black, with our branding incorporated in yellow and white for strong contrast and readability.

The banner should clearly communicate the full scope of services we provide, including:

Scaffold Design
Scaffold Engineering
Scaffold Installation / Erection
Scaffold Dismantling

It should also indicate the types of projects and clients we service, including:

Commercial
Industrial
Residential
Civil

The design should feel bold and professional, with a construction-oriented style that aligns with the scaffolding industry. It should be clean, impactful, and easy to read from a distance, ensuring passing traffic can quickly understand our services.

Where possible, subtle industrial or structural design elements (such as scaffold components, steel textures, or linework) may be incorporated into the background to reinforce the industry theme while keeping the layout uncluttered.

The final design will be produced as a large-format mesh banner for outdoor installation, so it should be created with this application and viewing distance in mind.

```html
<!DOCTYPE html>
<html lang="en">
<head>
<meta charset="utf-8">
<title>Rigmore Mesh Banner</title>
<link href="https://fonts.googleapis.com/css2?family=Montserrat:wght@700;800&display=swap" rel="stylesheet">
<style>
  :root {
    --brand-yellow: #f5ad1f;
    --brand-yellow-deep: #eaa318;
    --brand-black: #141414;
    --steel-dark: #1d1d1d;
    --white: #ffffff;
    --ink: #161616;
  }
  * { margin: 0; padding: 0; box-sizing: border-box; }
  html, body { width: 1200px; height: 216px; overflow: hidden; background: var(--brand-black); }
  .banner {
    position: relative;
    width: 1200px;
    height: 216px;
    overflow: hidden;
    font-family: "Montserrat", Arial, sans-serif;
    font-weight: 700;
    background: linear-gradient(100deg, var(--steel-dark), var(--brand-black) 60%, var(--steel-dark));
  }
  .banner-frame {
    position: absolute; inset: 0;
    border: 3px solid var(--brand-yellow);
    border-top-width: 0;
    pointer-events: none;
  }
  .shapes { position: absolute; inset: 0; }
  .brand {
    position: absolute;
    left: 0; top: 0;
    width: 320px; height: 216px;
    display: flex; align-items: center; justify-content: center; gap: 14px;
  }
  .brand-square { width: 18px; height: 18px; background: var(--brand-yellow); }
  .brand-name {
    color: var(--white);
    font-size: 34px;
    letter-spacing: 0.28em;
    text-transform: uppercase;
  }
  .heading {
    position: absolute;
    font-weight: 800;
    font-size: 35px;
    line-height: 1;
    letter-spacing: 0.005em;
  }
  .heading-rule { position: absolute; height: 2px; top: 57px; }
  .services-heading { left: 400px; width: 400px; top: 18px; text-align: center; color: var(--ink); }
  .services-rule { left: 547px; width: 106px; background: var(--white); }
  .industries-heading { left: 953px; top: 18px; color: var(--brand-yellow); }
  .industries-rule { left: 955px; width: 106px; background: var(--white); }
  .list { position: absolute; list-style: none; color: var(--white); font-size: 24.5px; line-height: 34px; }
  .services-list { left: 350px; width: 500px; top: 68px; text-align: center; }
  .industries-list { left: 954px; top: 68px; }
</style>
</head>
<body>
<div class="banner">
  <svg class="shapes" width="1200" height="216" viewBox="0 0 1200 216">
    <polygon class="chevron-left" points="368,19 315,143 368,205 330,143" fill="var(--white)"/>
    <polygon class="chevron-right" points="834,9 885,79 831,203 872,79" fill="var(--white)"/>
    <defs>
      <linearGradient id="panelTone" x1="0" y1="0" x2="1" y2="1">
        <stop offset="0" stop-color="var(--brand-yellow)"/>
        <stop offset="1" stop-color="var(--brand-yellow-deep)"/>
      </linearGradient>
    </defs>
    <polygon class="services-panel" role="img" aria-label="Yellow-toned photo of a steel warehouse roof frame"
      points="373,0 829,0 872,79 831,216 375,216 327,142" fill="url(#panelTone)"/>
  </svg>

  <div class="brand">
    <span class="brand-square"></span>
    <span class="brand-name">Rigmore</span>
  </div>

  <h2 class="heading services-heading">SERVICES</h2>
  <div class="heading-rule services-rule"></div>
  <ul class="list services-list">
    <li>Scaffold Design</li>
    <li>Scaffold Engineering</li>
    <li>Scaffold Installation / Erection</li>
    <li>Scaffold Dismantling</li>
  </ul>

  <h2 class="heading industries-heading">INDUSTRIES</h2>
  <div class="heading-rule industries-rule"></div>
  <ul class="list industries-list">
    <li>Commercial</li>
    <li>Industrial</li>
    <li>Residential</li>
    <li>Civil</li>
  </ul>

  <div class="banner-frame"></div>
</div>
</body>
</html>
```